Website design: Mobile Physiotherapy, Massage & Personal Training Business

I need a website that reflects a staff of health and fitness professionals. I would like the theme of the website to match the company logo (Summit Motion Wellness).
This is a link for a competitors website that I am fond of:
http://www.brackenrehab.com.au/
I am open to any and all creative and innovative designs.

```html
<!DOCTYPE html>
<html lang="en">
<head>
<meta charset="utf-8">
<title>Summit Motion Wellness</title>
<link href="https://fonts.googleapis.com/css2?family=Roboto+Slab:wght@300;400;700&family=Roboto:wght@400;500;700&family=Lobster&display=swap" rel="stylesheet">
<style>
:root{
  --red:#c8101e;
  --red-dark:#9e0c16;
  --ink:#2b2b2b;
  --grey:#555;
  --light:#e9e9e9;
  --line:#cfcfcf;
  --white:#fff;
}
*{margin:0;padding:0;box-sizing:border-box}
html,body{width:847px;height:1200px;overflow:hidden;background:var(--white)}
body{position:relative;font-family:Roboto,Arial,sans-serif;color:var(--ink)}
.abs{position:absolute}
.topbar{left:0;top:0;width:847px;height:3px;background:#222}
.header{left:0;top:3px;width:847px;height:92px;background:linear-gradient(#fff,#ececec)}
.brand{left:105px;top:40px;font-family:"Roboto Slab",serif;font-weight:700;font-size:20px;color:var(--red);display:flex;align-items:center;gap:8px}
.brand i{display:block;width:14px;height:14px;border-radius:50%;background:var(--red)}
.phone{left:630px;top:16px;display:flex;align-items:center;gap:6px;font-family:"Roboto Slab",serif;font-weight:700;font-size:15px;color:#333}
.nav{left:383px;top:52px;display:flex;align-items:center;font-family:"Roboto Slab",serif;font-size:10.5px;color:#222}
.nav span{padding:0 7px;border-left:1px solid #ccc;line-height:12px}
.nav span:first-child{border:0}
.nav .active{background:var(--red);color:#fff;padding:3px 7px;border-radius:2px;border:0}
.nav .active + span{border-left:0;margin-left:8px}
.slider{left:99px;top:109px;width:648px;height:264px;border:1px solid #ddd;border-radius:4px;background:#fff;box-shadow:0 12px 14px -12px rgba(0,0,0,.35)}
.slide{left:106px;top:116px;width:634px;height:251px;border-radius:5px;overflow:hidden}
.tagline{right:18px;top:74px;text-align:right;font-family:Lobster,cursive;font-size:27px;line-height:37px;color:#fff}
.dots{right:22px;bottom:10px;display:flex;gap:5px}
.dots i{width:10px;height:10px;border-radius:50%;background:#fff;display:block}
.service{width:210px;text-align:center}
.service .photo{width:96px;height:96px;border-radius:50%;margin:0 auto;border:2px solid #ddd}
.service h3{font-family:"Roboto Slab",serif;font-weight:400;font-size:12.5px;color:var(--red);margin-top:20px}
.service p{font-size:9.5px;line-height:13px;color:var(--grey);margin-top:13px}
.sec-head{display:flex;align-items:center;gap:4px;font-family:"Roboto Slab",serif;font-size:12.5px;color:#444}
.sec-head b{font-weight:400;color:var(--red)}
.sec-head svg{flex:none}
.dash{height:0;border-top:1px dashed var(--line)}
.welcome-text{left:100px;top:651px;width:418px;font-size:9.6px;line-height:13.2px;color:var(--grey);text-align:justify}
.author{left:100px;top:724px;font-family:"Roboto Slab",serif;font-weight:700;font-size:10.5px;color:var(--red-dark)}
.role{left:100px;top:738px;font-size:10.5px;color:#444}
.more{left:458px;top:750px;font-size:9.5px;color:var(--red)}
.vdiv{left:532px;width:1px;background:#ddd}
.field{left:551px;width:187px;height:18px;border:1px solid #bbb;border-radius:2px;background:#fff;font-size:8.5px;color:#333;padding:3px 9px;box-shadow:inset 0 1px 2px rgba(0,0,0,.12)}
.submit{left:551px;top:776px;width:49px;height:19px;background:#2a2a2a;border:1px solid #000;border-radius:2px;color:#fff;font-size:10px;font-weight:700;text-align:center;line-height:17px}
.arrows{left:474px;top:818px;font-size:15px;color:#777;letter-spacing:5px}
.blog{left:99px;top:853px;width:409px;height:100px;background:var(--light);border-radius:8px}
.post{top:14px;display:flex;gap:10px}
.avatar{width:72px;height:72px;border-radius:50%;border:2px solid #fff;background:linear-gradient(#e4e1de,#8a7a72 55%,#2d2a2b);flex:none}
.post-text{font-size:9.5px;line-height:13px;color:#666;width:110px}
.post-text strong{color:#333;font-weight:500}
.video{left:552px;top:853px;width:183px;height:101px;background:linear-gradient(100deg,#c9b48a 0%,#7d6a4e 30%,#55534f 55%,#9aa0a6 80%,#3b3b3b 100%)}
.video .bar{position:absolute;left:0;bottom:0;width:100%;height:10px;background:#111}
.partner{top:1010px;height:42px}
.footer-wave{left:0;top:990px}
.f-col,.f-brand,.copy{color:var(--white)}
.f-col h4{font-family:"Roboto Slab",serif;font-weight:300;font-size:14px;margin-bottom:11px;color:var(--white)}
.f-col p{font-size:9.2px;line-height:16.3px;color:var(--white)}
.f-div{top:1086px;height:100px;border-left:1px dashed rgba(255,255,255,.45)}
.contact-row{display:flex;gap:10px;font-size:8.5px;line-height:11px;margin-bottom:6px;color:var(--white)}
.contact-row svg{flex:none}
.f-brand{left:640px;top:1096px;width:110px;text-align:center;font-family:"Roboto Slab",serif;font-weight:700;font-size:12px;line-height:14px}
.social{left:645px;top:1136px;display:flex;gap:5px}
.social i{display:block;width:18px;height:18px;border-radius:50%;border:1.5px solid #fff;background:rgba(255,255,255,.2)}
.copy{left:630px;top:1163px;width:130px;text-align:center;font-size:8.5px;line-height:12px}
</style>
</head>
<body>
<div class="abs topbar"></div>
<header class="abs header"></header>
<div class="abs brand"><i></i>Summit Motion Wellness</div>
<div class="abs phone">
  <svg width="20" height="20" viewBox="0 0 20 20"><circle cx="10" cy="10" r="9" fill="none" stroke="#333" stroke-width="1.6"/><path d="M7 5.5l2 2-1 1.3c.6 1.3 1.5 2.2 2.7 2.7l1.3-1 2 2-1.2 1.5C9.6 13.6 6.6 10.6 5.6 7z" fill="#333"/></svg>
  012-555-0198
</div>
<nav class="abs nav"><span class="active">HOME</span><span>ABOUT US</span><span>OUR SERVICES ⌄</span><span>PRODUCTS ⌄</span><span>CONTACT US</span></nav>

<div class="abs slider"></div>
<div class="abs slide">
  <svg width="634" height="251" viewBox="0 0 634 251">
    <defs>
      <linearGradient id="lake" x1="0" y1="0" x2="0" y2="1"><stop offset="0" stop-color="#26401f"/><stop offset=".25" stop-color="#4d6e3a"/><stop offset=".42" stop-color="#3a5538"/><stop offset=".48" stop-color="#6f8288"/><stop offset=".7" stop-color="#4f6068"/><stop offset="1" stop-color="#1f2b30"/></linearGradient>
      <linearGradient id="redp" x1="0" y1="0" x2="0" y2="1"><stop offset="0" stop-color="#e0141f"/><stop offset="1" stop-color="#a40f18"/></linearGradient>
    </defs>
    <rect width="634" height="251" fill="url(#lake)" role="img" aria-label="Photo of a rower sculling on a calm lake with forest behind"/>
    <path d="M512 0 C 545 70 520 200 250 251 L634 251 L634 0 Z" fill="#151515"/>
    <path d="M524 0 C 555 75 525 205 264 251 L634 251 L634 0 Z" fill="url(#redp)"/>
  </svg>
  <div class="abs tagline">Mobile Health &amp;<br>Fitness Service<br>- Gold Coast</div>
  <div class="abs dots"><i></i><i></i><i></i><i></i></div>
</div>

<section class="abs service" style="left:91px;top:402px">
  <div class="photo" role="img" aria-label="Physiotherapist stretching a client's leg" style="background:linear-gradient(160deg,#f4f1ee 0%,#e3cfc2 40%,#3f69ad 70%,#2a2a36 100%)"></div>
  <h3>PHYSIOTHERAPY</h3>
  <p>Lorem ipsum dolor sit amet, consectetuer adipiscing elit, sed diam nonummy nibh euismod tincidunt ut.</p>
</section>
<section class="abs service" style="left:315px;top:402px">
  <div class="photo" role="img" aria-label="Client relaxing during a back massage" style="background:linear-gradient(170deg,#f6f2ec 0%,#e8d2c0 45%,#b98062 75%,#5a3a2e 100%)"></div>
  <h3>MASSAGE</h3>
  <p>Lorem ipsum dolor sit amet, consectetuer adipiscing elit, sed diam nonummy nibh euismod tincidunt ut.</p>
</section>
<section class="abs service" style="left:540px;top:402px">
  <div class="photo" role="img" aria-label="Trainer coaching a client with dumbbells in a gym" style="background:linear-gradient(180deg,#45608e 0%,#8a9fc4 35%,#e9e6e4 65%,#5b6c8a 100%)"></div>
  <h3>PERSONAL TRAINING</h3>
  <p>Lorem ipsum dolor sit amet, consectetuer adipiscing elit, sed diam nonummy nibh euismod tincidunt ut.</p>
</section>

<div class="abs sec-head" style="left:99px;top:604px"><svg width="30" height="26"><circle cx="15" cy="13" r="5" fill="#c8101e"/></svg>WELCOME TO&nbsp;<b>SUMMIT MOTION WELLNESS</b></div>
<div class="abs dash" style="left:99px;top:639px;width:416px"></div>
<p class="abs welcome-text">Lorem ipsum dolor sit amet, consectetuer adipiscing elit, sed diam nonummy nibh euismod tincidunt ut laoreet dolore magna aliquam erat volutpat. Ut wisi enim ad minim veniam, quis nostrud exerci tation ullamcorper suscipit lobortis nisl ut aliquip ex ea commodo consequat. Duis autem vel eum iriure dolor in hendrerit in vulputate velit esse molestie consequat, vel illum dolore eu feugiat nulla facilisis at vero eros et accumsan et iusto odio eu.</p>
<div class="abs author">Morgan Halloway</div>
<div class="abs role">Dr. of Physiotherapy and B. Ex. Science.</div>
<div class="abs more">Read More &gt;&gt;</div>

<div class="abs vdiv" style="top:612px;height:188px"></div>
<div class="abs vdiv" style="top:818px;height:140px"></div>

<div class="abs sec-head" style="left:550px;top:604px"><svg width="30" height="26"><circle cx="15" cy="13" r="5" fill="#c8101e"/></svg>QUICK&nbsp;<b>CONTACT</b></div>
<div class="abs dash" style="left:548px;top:639px;width:195px"></div>
<div class="abs field" style="top:654px">Name</div>
<div class="abs field" style="top:678px">Email</div>
<div class="abs field" style="top:702px">Phone</div>
<div class="abs field" style="top:726px;height:43px">Message</div>
<div class="abs submit">Submit</div>

<div class="abs sec-head" style="left:99px;top:812px"><svg width="30" height="26"><circle cx="15" cy="13" r="5" fill="#c8101e"/></svg>RECENT&nbsp;<b>BLOG POSTS</b></div>
<div class="abs arrows">&lt;&gt;</div>
<div class="abs blog">
  <div class="abs post" style="left:9px"><div class="avatar" role="img" aria-label="Blog author portrait"></div><div class="post-text"><strong>Lorem ipsum</strong> 1Jun,2014<br>Loremdolor this is ipsum dolor this is a sit amet consectetuer adipiscing elit, sed diam.</div></div>
  <div class="abs post" style="left:216px"><div class="avatar" role="img" aria-label="Blog author portrait"></div><div class="post-text"><strong>Lorem ipsum</strong> 1Jun,2014<br>Loremdolor this is ipsum dolor this is a sit amet consectetuer adipiscing elit, sed diam.</div></div>
</div>

<div class="abs sec-head" style="left:552px;top:812px"><svg width="30" height="26"><circle cx="15" cy="13" r="5" fill="#c8101e"/></svg>HOW WE&nbsp;<b>CAN HELP YOU</b></div>
<div class="abs video" role="img" aria-label="Video still of two people training on gym machines">
  <svg class="abs" style="left:80px;top:38px" width="24" height="24"><circle cx="12" cy="12" r="11" fill="rgba(255,255,255,.6)"/><path d="M9 6l9 6-9 6z" fill="#fff"/></svg>
  <div class="bar"></div>
</div>

<div class="abs sec-head" style="left:99px;top:969px"><svg width="30" height="26"><circle cx="15" cy="13" r="5" fill="#c8101e"/></svg>TRUSTED&nbsp;<b>BY</b></div>
<div class="abs partner" style="left:102px;width:94px;background:#e6eef8;border-radius:3px"></div>
<div class="abs partner" style="left:219px;width:35px;background:#1f3f7a"></div>
<div class="abs partner" style="left:278px;width:125px;background:#e8eef6;border-radius:21px"></div>

<svg class="abs footer-wave" width="847" height="210" viewBox="0 0 847 210">
  <defs><linearGradient id="fg" x1="0" y1="0" x2="0" y2="1"><stop offset="0" stop-color="#c8101e" stop-opacity="0"/><stop offset="1" stop-color="#8f0c14"/></linearGradient></defs>
  <path d="M0 80 C300 76 600 50 847 0 L847 14 C600 64 300 84 0 86 Z" fill="#111"/>
  <path d="M0 86 C300 84 600 64 847 14 L847 210 L0 210 Z" fill="#c8101e"/>
  <rect y="90" width="847" height="120" fill="url(#fg)"/>
</svg>

<div class="abs f-col" style="left:101px;top:1082px">
  <h4>Quick Links</h4>
  <p>&gt; Home<br>&gt; About Us<br>&gt; Our Services<br>&gt; Products<br>&gt; Contact Us</p>
</div>
<div class="abs f-div" style="left:216px"></div>
<div class="abs f-col" style="left:255px;top:1082px">
  <h4>Contact Info</h4>
  <div class="contact-row"><svg width="9" height="12"><path d="M4.5 0a4.5 4.5 0 0 1 4.5 4.5C9 8 4.5 12 4.5 12S0 8 0 4.5A4.5 4.5 0 0 1 4.5 0z" fill="#fff"/><circle cx="4.5" cy="4.5" r="1.6" fill="#c8101e"/></svg><span>Street Name, City Name<br>Zip Code-00000</span></div>
  <div class="contact-row"><svg width="11" height="11"><path d="M2 1l3 3-1.3 1.5c.7 1.3 1.6 2.2 2.8 2.8L8 7l3 3-1.6 1.3C5 10 1 6 0 2.6z" fill="#fff"/></svg><span>0412 555 019</span></div>
  <div class="contact-row"><svg width="11" height="11"><rect x="2" y="0" width="7" height="4" fill="#fff"/><rect x="0" y="4" width="11" height="5" rx="1" fill="#fff"/><rect x="2" y="7" width="7" height="4" fill="#fff" stroke="#c8101e"/></svg><span>123-5550-144</span></div>
  <div class="contact-row"><svg width="11" height="9"><rect width="11" height="9" fill="#fff"/><path d="M0 0l5.5 5 5.5-5" fill="none" stroke="#c8101e"/></svg><span>hello@summitmotionwellness.com</span></div>
</div>
<div class="abs f-div" style="left:435px"></div>
<div class="abs f-col" style="left:474px;top:1082px">
  <h4>Trading Hours</h4>
  <p><b>Monday To Friday</b><br>5am-7pm</p>
  <p style="margin-top:9px"><b>Sat</b> 7-11.30</p>
  <p style="margin-top:7px"><b>Sunday</b> Closed</p>
</div>
<div class="abs f-div" style="left:603px"></div>
<div class="abs f-brand">Summit Motion<br>Wellness</div>
<div class="abs social"><i></i><i></i><i></i><i></i></div>
<div class="abs copy">© Summit Motion Wellness<br>All Rights Reserved.</div>
</body>
</html>
```